Moltven Advisory e-Flyer Design

Need 6 or so one pagers done. To be used to email to clients. Each to look similar with slight variations. Attached is an example done for a completely different organization, but it has the style we are looking for, and it is energetic and corporate.

```html
<!DOCTYPE html>
<html lang="en">
<head>
<meta charset="utf-8">
<title>Moltven Advisory – Services Flyer</title>
<link rel="stylesheet" href="https://fonts.googleapis.com/css2?family=Open+Sans:wdth,wght@75..100,300..800&display=swap">
<style>
  :root{
    --red:#d0202e;
    --navy:#0e2a52;
    --band:#bdbdbd;
    --green:#8fc04a;
    --ink:#333333;
    --white:#ffffff;
    --photo-a:#3b3a3c;
    --photo-b:#b58a63;
    --photo-c:#e9d6b6;
  }
  *{box-sizing:border-box;margin:0;padding:0}
  html,body{width:848px;height:1200px;overflow:hidden;background:var(--white)}
  body{font-family:"Open Sans",Arial,sans-serif;font-stretch:75%;color:var(--ink);position:relative}

  .hero-photo{position:absolute;left:326px;top:0;width:522px;height:441px;
    background:linear-gradient(160deg,var(--photo-c) 0%,var(--photo-b) 30%,var(--photo-a) 65%,#2a2a2c 100%)}
  .tagline-band{position:absolute;left:197px;top:50px;width:651px;height:76px;background:var(--band);opacity:.93;
    display:flex;flex-direction:column;justify-content:center;padding-left:30px}
  .tagline-band p{color:var(--white);font-weight:700;font-size:19.5px;line-height:29px;text-transform:uppercase;white-space:nowrap}

  .brand{position:absolute;left:47px;top:40px;width:145px}
  .brand-square{display:block;width:22px;height:22px;background:var(--red);margin-bottom:10px}
  .brand-name{display:block;color:var(--red);font-weight:600;font-size:27px;line-height:31px;text-transform:uppercase}

  .about{position:absolute;left:47px;top:190px;width:265px}
  .about h2{color:var(--red);font-weight:400;font-size:25px;line-height:30px;text-transform:uppercase}
  .about p{font-size:9.6px;line-height:12.5px;margin-bottom:9px}
  .about .values{font-size:17px;line-height:22px}

  .services{position:absolute;left:0;top:441px;width:848px;height:692px;background:var(--navy);color:var(--white);padding:16px 47px 0}
  .services h2{font-weight:400;font-size:24px;line-height:30px;padding-bottom:10px;border-bottom:1px dotted rgba(255,255,255,.7);margin-bottom:2px}
  .service{border-bottom:1px dotted rgba(255,255,255,.7);padding-bottom:7px;margin-bottom:4px}
  .service:last-child{border-bottom:none}
  .service h3{color:var(--green);font-weight:400;font-size:25px;line-height:30px}
  .service .lead{font-size:17.5px;line-height:25px;font-weight:400}
  .service ul{list-style:none;margin-top:2px}
  .service li{font-size:8.9px;line-height:12.2px;padding-left:9px;position:relative;margin-bottom:1.6px}
  .service li::before{content:"•";position:absolute;left:0}

  .contact{position:absolute;left:0;top:1133px;width:848px;height:67px;display:flex;align-items:center;justify-content:center}
  .contact p{color:var(--red);font-weight:700;font-size:18.5px;letter-spacing:.2px;text-transform:uppercase}
</style>
</head>
<body>
  <div class="hero-photo" role="img" aria-label="Busy city street at sunset with crowds of commuters walking toward the camera"></div>

  <div class="tagline-band">
    <p>Moltven Advisory is unique global management consultancy.</p>
    <p>We convert strategy into action, and action into results.</p>
  </div>

  <div class="brand">
    <span class="brand-square"></span>
    <span class="brand-name">Moltven<br>Advisory</span>
  </div>

  <section class="about">
    <h2>Who we are</h2>
    <p>Moltven Advisory operates in the US, Europe, Asia, Australia and New Zealand. The Moltven Advisory team consists of highly experienced corporate executives with a track record of delivering transformational programs to organizations across industries, both commercial and not for profit, large and small, to achieve higher performance.</p>
    <h2>Mission</h2>
    <p>To partner with organizations to ignite and empower them around a clear strategy, and facilitate efficient and fully integrated execution, to deliver higher performance.</p>
    <h2>Values</h2>
    <p class="values">Ignite, Empower, Deliver</p>
  </section>

  <section class="services">
    <h2>SERVICES</h2>

    <div class="service">
      <h3>Ignition</h3>
      <p class="lead">Ignite is a proven, proprietary method to bring cohesion to a tea to create a shared understanding of what they want to achieve and how they will galvanize the organization to achieve it.</p>
      <ul>
        <li>Effective dialogue is the most productive way to truly harness the collective intellect of a team and organization.</li>
        <li>Moltven Advisory uses a tested process, Ignition, to create a space for great dialog for teams of up to 300 people.</li>
        <li>The Ignite process is tailored for each client to clarify strategy, define the execution path, strengthen team cohesion and ignite momentum.</li>
        <li>Ignition happens at speed to create a bridge for the present state to the future state.</li>
        <li>Ignition is purposely built to create ownership by the team.</li>
        <li>Ignition frequently produces breakthroughs and is about unleashing what a collective can achieve together.</li>
      </ul>
    </div>

    <div class="service">
      <h3>Strategy Clarification</h3>
      <p class="lead">Knowing what organization wants to be in 3-5 years time is a competitive advantage.</p>
      <ul>
        <li>Concisely exploring the alternatives and selecting on objective and strategy for the strategic horizon is a comparative advantage for organizations that undertake a proper strategic planning process including understanding evolving customer needs, competitive differentiation, and the critical capabilities required to compete and win.</li>
        <li>Research shows that organizations that are executing against a clear strategy outperform those that do not, even if the choice of strategy ultimately proves to be incorrect, largely due to deliberate intent and discipline.</li>
        <li>Having a 3-5 year strategy is critical to allowing the organization to have a coherent direction which all stakeholders can support, make strategic investments in future capabilities, and outperform the competition.</li>
      </ul>
    </div>

    <div class="service">
      <h3>Executional Alignment</h3>
      <p class="lead">Strategy is just an exercise unless it is executed effectively and becomes the operating blueprint of the organization.</p>
      <ul>
        <li>Strategy a critical starting point to set objective and direction for the 3 year horizon, however without the organization executing against strategy, it is academic.</li>
        <li>Driving executional alignment to the strategy is critical to success, and requires the organization to consciously align the operations of the business to the strategy.</li>
        <li>Executional alignment requires overcoming the inertia of Business as Usual by enabling change through all aspects of the organization, identifying and removing barriers, beginning with a culture of embracing the strategy and competing to win.</li>
      </ul>
    </div>

    <div class="service">
      <h3>Leadership Development</h3>
      <p class="lead">Having the right leadership capability is the difference between success and failure.</p>
      <ul>
        <li>Every organization is comprised of unique people with different styles, experience and expertise.</li>
        <li>Ensuring leaders at all levels of the organization are suitably developed and equipped to do the best job is critical to outperform the competition and being on employer of choice to retain talented employees.</li>
        <li>The skills of leadership are evolving with changing demographics, technology, increased understanding of the benefits of diversity, a premium on innovation, amongst other macro trends, and organizations need to ensure their leaders have the knowledge and capabilities to manage these changes effectively.</li>
      </ul>
    </div>

    <div class="service">
      <h3>Cultural Transformation</h3>
      <p class="lead">Organizational culture can evolve organically, or it can be seen as a business asset that is consciously managed.</p>
      <ul>
        <li>Organizations that choose the culture they desire are leveraging one of the most important business assets available, one that is often to evolve without overt consideration.</li>
        <li>Placing clear focus on the desired culture and having initiative to achieve this, and monitoring performance against the intent, is a competitive differentiator.</li>
      </ul>
    </div>
  </section>

  <footer class="contact">
    <p>For more information: call +1 212 555 0147, email info@moltvenadvisory.com</p>
  </footer>
</body>
</html>
```